Business Card Design

Online clothing womens clothing store, I sell my clothing online and at the markets.

i would like the attached picture on the front of the card and the contact information on the back.

Industry/Entity Type

Business

Contact Information for Business Card

Velvet Harbour
Marnie Talbot
(Instagram symbol) _velvet_harbour_
(Facebook symbol) www.facepage-example.com/velvetharbourau/

W : www.velvetharbour-example.com.au
E : info@velvetharbour-example.com.au
P : 0491876324

```html
<!DOCTYPE html>
<html lang="en">
<head>
<meta charset="UTF-8">
<title>Velvet Harbour – Business Card</title>
<link rel="stylesheet" href="https://fonts.googleapis.com/css2?family=Open+Sans:wght@400;600;700&display=swap">
<style>
  :root {
    --backdrop: #3b322d;
    --card-black: #141414;
    --ink-white: #f2f2f2;
    --ink-soft: #d9d9d9;
    --rule: #8a8a8a;
    --mist-light: #eef0f1;
    --mist-mid: #c5cbd0;
    --mist-dark: #5d6470;
  }
  * { box-sizing: border-box; margin: 0; padding: 0; }
  html, body {
    width: 1200px;
    height: 844px;
    overflow: hidden;
  }
  body {
    background: var(--backdrop);
    font-family: "Open Sans", Arial, sans-serif;
    position: relative;
  }
  .card {
    position: absolute;
    top: 274px;
    width: 520px;
    height: 297px;
    overflow: hidden;
  }
  /* Contact side */
  .card-back {
    left: 60px;
    background: var(--card-black);
    color: var(--ink-white);
  }
  .holder-name {
    position: absolute;
    left: 30px;
    top: 156px;
    font-size: 18px;
    font-weight: 600;
    letter-spacing: 0.3px;
    text-transform: uppercase;
  }
  .divider {
    position: absolute;
    left: 198px;
    top: 92px;
    width: 1px;
    height: 112px;
    background: var(--rule);
  }
  .contact-list {
    position: absolute;
    left: 212px;
    top: 92px;
    list-style: none;
    font-size: 12px;
    line-height: 19px;
    color: var(--ink-soft);
  }
  .contact-list li {
    display: flex;
    align-items: center;
    gap: 8px;
    white-space: nowrap;
  }
  .contact-list li.group-break { margin-top: 10px; }
  .contact-icon {
    width: 12px;
    height: 12px;
    flex: none;
  }
  .social-mark {
    width: 9px;
    height: 9px;
    margin: 0 1.5px;
    background: var(--ink-soft);
    flex: none;
  }
  /* Brand side */
  .card-front {
    left: 620px;
    background:
      radial-gradient(ellipse 60% 75% at 72% 30%, var(--mist-dark) 0%, rgba(93,100,112,0.55) 45%, rgba(197,203,208,0) 80%),
      linear-gradient(160deg, var(--mist-light) 0%, var(--mist-mid) 100%);
  }
  .brand-name {
    position: absolute;
    right: 22px;
    bottom: 22px;
    font-size: 40px;
    font-weight: 700;
    letter-spacing: 4px;
    text-transform: uppercase;
    color: #ffffff;
  }
</style>
</head>
<body>

  <section class="card card-back" aria-label="Card back with contact details">
    <p class="holder-name">Marnie Talbot</p>
    <div class="divider"></div>
    <ul class="contact-list">
      <li>
        <svg class="contact-icon" viewBox="0 0 12 12" aria-hidden="true"><path d="M2.5 1h2l1 2.6-1.3 1a6 6 0 0 0 2.7 2.7l1-1.3L11 7v2a1.5 1.5 0 0 1-1.5 1.5A8.5 8.5 0 0 1 1 2.5 1.5 1.5 0 0 1 2.5 1z" fill="#d9d9d9"/></svg>
        <span>0491876324</span>
      </li>
      <li>
        <svg class="contact-icon" viewBox="0 0 12 12" aria-hidden="true"><rect x="1" y="2.5" width="10" height="7" fill="#d9d9d9"/><path d="M1 2.5l5 4 5-4" fill="none" stroke="#141414" stroke-width="1.1"/></svg>
        <span>info@velvetharbour-example.com.au</span>
      </li>
      <li>
        <svg class="contact-icon" viewBox="0 0 12 12" aria-hidden="true"><g fill="none" stroke="#d9d9d9" stroke-width="1.3"><rect x="1.2" y="5" width="5" height="3" rx="1.5" transform="rotate(-45 3.7 6.5)"/><rect x="5.8" y="4" width="5" height="3" rx="1.5" transform="rotate(-45 8.3 5.5)"/></g></svg>
        <span>www.velvetharbour-example.com.au</span>
      </li>
      <li class="group-break">
        <span class="social-mark" aria-hidden="true"></span>
        <span>_velvet_harbour_</span>
      </li>
      <li>
        <span class="social-mark" aria-hidden="true"></span>
        <span>www.facepage-example.com/velvetharbourau/</span>
      </li>
    </ul>
  </section>

  <section class="card card-front" role="img" aria-label="Misty grey-blue photograph chosen by the shop owner, fading to pale white, with the brand name across the lower edge">
    <p class="brand-name">Velvet Harbour</p>
  </section>

</body>
</html>
```